Tasman Curdworks Guild needs new business cards

We need new business cards designed and produced. We are likely to need other design work done for ads, flyers etc in future.

We would like to start with an initial business card.

The Tasman Curdworks Guild (TCG) is a membership-based not-for-profit organisation that looks after the interests of Australia's small to medium artisan cheesemakers, many of whom are also small-scale farmers. The design should be simple, using our logo, but also communicate our artisan cheese and small dairy farm focus.

The first card to be designed and produced is for me, Miriam Tolhurst. My details are:

Miriam Tolhurst
Secretary
Tasman Curdworks Guild (TCG)
http://www.curdworksguild.example
T +61452837190
E miriam.miriamtolhurst@mailbox.example

I have attached the TCG logo in jpg form. I have a higher resolution version available if needed.

Thank you!

Miriam

Miriam Tolhurst
Tasman Curdworks Guild
miriam.miriamtolhurst@mailbox.example
+61452837190

Sans Serif

• Logo (see attached file)

```html
<!DOCTYPE html>
<html lang="en">
<head>
<meta charset="utf-8">
<title>Tasman Curdworks Guild – Business Cards</title>
<link rel="stylesheet" href="https://fonts.googleapis.com/css2?family=Roboto+Slab:wght@400;700&family=Roboto+Condensed:wght@700&display=swap">
<style>
  :root {
    --brown: #524132;
    --cheese: #fec96c;
    --paper: #f2f2f2;
    --paper-soft: #e8e8e8;
    --white: #ffffff;
    --backdrop: #ebe6e0;
  }
  html, body {
    margin: 0;
    padding: 0;
    width: 1200px;
    height: 1200px;
    overflow: hidden;
    background: var(--backdrop);
  }
  .card {
    position: absolute;
    left: 180px;
    width: 840px;
    height: 480px;
    background: var(--paper);
    box-shadow: 0 6px 16px rgba(60, 40, 20, 0.18);
    overflow: hidden;
    font-family: "Roboto Slab", Georgia, serif;
    color: var(--brown);
  }
  .card--front { top: 120px; }
  .card--back {
    top: 644px;
    background: radial-gradient(ellipse at 48% 45%, #ffffff 0%, var(--paper) 45%, var(--paper-soft) 100%);
  }
  .block { position: absolute; }
  .header-band { left: 0; top: 0; width: 714px; height: 102px; background: var(--brown); }
  .header-rule { left: 0; top: 105px; width: 714px; height: 4px; background: var(--brown); }
  .header-tab { left: 734px; top: 0; width: 106px; height: 102px; background: var(--cheese); }
  .header-tab-rule { left: 734px; top: 105px; width: 106px; height: 3px; background: var(--cheese); }
  .org-name {
    position: absolute;
    left: 36px;
    top: 72px;
    margin: 0;
    font-size: 20px;
    font-weight: 700;
    color: var(--white);
    text-transform: uppercase;
    letter-spacing: 0.5px;
    line-height: 1;
  }
  .org-acronym {
    position: absolute;
    left: 741px;
    top: 72px;
    margin: 0;
    font-size: 20px;
    font-weight: 700;
    color: var(--brown);
    line-height: 1;
  }
  .person-name {
    position: absolute;
    left: 94px;
    top: 196px;
    margin: 0;
    font-size: 46px;
    font-weight: 700;
    line-height: 1;
    letter-spacing: -0.5px;
  }
  .person-role {
    position: absolute;
    left: 94px;
    top: 240px;
    margin: 0;
    font-size: 36px;
    font-weight: 400;
    line-height: 1;
  }
  .guild-mark {
    position: absolute;
    left: 560px;
    top: 168px;
    width: 180px;
    display: flex;
    align-items: center;
    gap: 12px;
  }
  .guild-mark__dot {
    flex: 0 0 34px;
    height: 34px;
    border-radius: 50%;
    background: var(--cheese);
  }
  .guild-mark__name {
    font-size: 19px;
    font-weight: 700;
    line-height: 1.2;
    color: var(--brown);
  }
  .footer-tab-rule { left: 0; top: 354px; width: 72px; height: 3px; background: var(--cheese); }
  .footer-tab { left: 0; top: 358px; width: 72px; height: 122px; background: var(--cheese); }
  .footer-rule { left: 94px; top: 356px; width: 746px; height: 4px; background: var(--brown); }
  .footer-band { left: 94px; top: 362px; width: 746px; height: 118px; background: var(--brown); }
  .phone {
    position: absolute;
    left: 152px;
    top: 403px;
    margin: 0;
    font-family: "Roboto Condensed", "Arial Narrow", sans-serif;
    font-size: 36px;
    font-weight: 700;
    color: var(--white);
    letter-spacing: 1px;
    line-height: 1;
  }
  .contact-divider { left: 426px; top: 392px; width: 2px; height: 54px; background: var(--white); }
  .contact-list {
    position: absolute;
    left: 444px;
    top: 386px;
    margin: 0;
    padding: 0;
    list-style: none;
    color: var(--white);
    font-size: 18px;
    line-height: 36px;
  }
</style>
</head>
<body>

<article class="card card--front">
  <div class="block header-band"></div>
  <div class="block header-rule"></div>
  <div class="block header-tab"></div>
  <div class="block header-tab-rule"></div>
  <p class="org-name">Tasman Curdworks Guild</p>
  <p class="org-acronym">(TCG)</p>
  <h1 class="person-name">MIRIAM TOLHURST</h1>
  <p class="person-role">Secretary</p>
  <div class="guild-mark">
    <span class="guild-mark__dot"></span>
    <span class="guild-mark__name">Tasman Curdworks Guild</span>
  </div>
  <div class="block footer-tab-rule"></div>
  <div class="block footer-tab"></div>
  <div class="block footer-rule"></div>
  <div class="block footer-band"></div>
  <p class="phone">+61452837190</p>
  <div class="block contact-divider"></div>
  <ul class="contact-list">
    <li>W: www.curdworksguild.example</li>
    <li>E: miriam.miriamtolhurst@mailbox.example</li>
  </ul>
</article>

<article class="card card--back">
  <div class="block header-band"></div>
  <div class="block header-rule"></div>
  <div class="block header-tab"></div>
  <div class="block header-tab-rule"></div>
  <p class="org-name">Tasman Curdworks Guild</p>
  <p class="org-acronym">(TCG)</p>
  <h2 class="person-name">MIRIAM TOLHURST</h2>
  <p class="person-role">Secretary</p>
  <div class="guild-mark">
    <span class="guild-mark__dot"></span>
    <span class="guild-mark__name">Tasman Curdworks Guild</span>
  </div>
  <div class="block footer-tab-rule"></div>
  <div class="block footer-tab"></div>
  <div class="block footer-rule"></div>
  <div class="block footer-band"></div>
  <p class="phone">+61452837190</p>
  <div class="block contact-divider"></div>
  <ul class="contact-list">
    <li>W: www.curdworksguild.example</li>
    <li>E: miriam.miriamtolhurst@mailbox.example</li>
  </ul>
</article>

</body>
</html>
```